Trendy eye catching business card for lawn mowing business

Verge Crew, a local community lawn mowing service, requires an eye catching trendy business card to drop into letterboxes.

We could simply throw something together from a Microsoft Word template, but we are wanting something more than this. Some other business’ images are attached for some inspiration.

We are requiring the card to have Verge Crew with our slogan, Call The Pellows. In addition, provide details with that we are a local, affordable lawn mowing service, and for other gardening matters to simply just ask!
Plus the relevant contact details, phone, email, social media.

Target Market(s)

Local community members who require assistance with their garden care

Industry/Entity Type

Gardening

Contact Information for Business Card

the name VERGE CREW is our logo
telephone logo 0493 218 067
email logo vergecrew@postbox-example.com
Instagram logo vergecrew
Facebook logo vergecrew.sth
Lawn Mowing Service
Local Affordable
edge trim, blow and clipping removal included.
Other gardening matters, just ask!

Font styles to use
Serif
Sans Serif
Decorative
Script

Colors
9bcb3c
ffffff

Requirements
Must have
• All the details listed in Business Card Details.
Make these words prominent:
Verge Crew
Lawn Mowing Service
Local
Affordable
Nice to have
• Our slogan ‘Call The Pellows’ incorporated.
Different colour background for front and reverse side
Greens, white and black colours
Subtle grass blades images incorporated
Should not have
• No images of lawnmowers.
No images of men/cartoons.
No using initials for Verge Crew

```html
<!DOCTYPE html>
<html lang="en">
<head>
<meta charset="utf-8">
<title>Verge Crew – Business Card</title>
<link rel="stylesheet" href="https://fonts.googleapis.com/css2?family=Poppins:wght@400;700;800&family=Barlow+Condensed:wght@400&family=Allura&display=swap">
<style>
  :root {
    --backdrop: #262626;
    --front-bg: #e9f5d8;
    --back-bg: #0c5d1d;
    --forest: #15592a;
    --leaf: #55b82e;
    --leaf-deep: #46a51f;
    --ink: #3a3a3a;
    --white: #ffffff;
  }
  * { margin: 0; padding: 0; box-sizing: border-box; }
  html, body {
    width: 1125px; height: 1200px; overflow: hidden;
    background: var(--backdrop);
    font-family: "Poppins", sans-serif;
  }
  .canvas { position: relative; width: 1125px; height: 1200px; }
  .card {
    position: absolute; left: 171px; width: 826px; height: 471px;
    box-shadow: 0 6px 14px rgba(0,0,0,.45);
  }
  .card--front { top: 106px; background: var(--front-bg); }
  .card--back { top: 639px; background: var(--back-bg); text-align: center; }

  /* front */
  .brand {
    position: absolute; left: 96px; top: 158px; width: 300px;
    display: flex; flex-direction: column; align-items: center;
    color: var(--forest); font-weight: 800; line-height: 1;
  }
  .brand__name-top { font-size: 72px; letter-spacing: -1px; }
  .brand__name-bottom { font-size: 56px; letter-spacing: 0; margin-top: 2px; }
  .brand__slogan {
    font-family: "Allura", cursive; font-weight: 400;
    color: var(--leaf); font-size: 42px; margin-top: -2px;
  }
  .divider {
    position: absolute; left: 417px; top: 164px; width: 2px; height: 142px;
    background: var(--forest);
  }
  .contact { position: absolute; left: 455px; top: 163px; }
  .contact__name {
    font-size: 29px; font-weight: 700; color: var(--forest); letter-spacing: .3px;
    line-height: 1.2; margin-bottom: 16px;
  }
  .contact__list { list-style: none; }
  .contact__item {
    display: flex; align-items: center; gap: 10px;
    font-size: 18.5px; color: var(--ink); line-height: 22.7px;
  }
  .contact__icon { width: 16px; height: 16px; flex: none; }

  /* back */
  .service {
    position: absolute; left: 0; right: 0; top: 70px;
    font-size: 51px; font-weight: 800; color: var(--leaf-deep); letter-spacing: -.5px; line-height: 1.2;
  }
  .qualities {
    position: absolute; left: 0; right: 0; top: 127px;
    font-size: 39px; font-weight: 700; color: var(--leaf-deep); letter-spacing: .5px; line-height: 1.2;
  }
  .qualities__sep { display: inline-block; width: 2px; height: 32px; background: var(--leaf-deep); margin: 0 16px; vertical-align: -3px; }
  .includes {
    position: absolute; left: 0; right: 0; top: 222px;
    font-family: "Barlow Condensed", sans-serif; font-size: 33px; color: var(--white); letter-spacing: .8px; line-height: 1;
  }
  .includes__text { border-bottom: 2px solid var(--leaf-deep); padding-bottom: 4px; }
  .extras {
    position: absolute; left: 0; right: 0; top: 260px;
    font-size: 28px; font-weight: 400; color: var(--white); letter-spacing: .5px; line-height: 1.2;
  }
  .extras__ask { font-weight: 800; color: var(--leaf-deep); }
  .hotline {
    position: absolute; left: 0; right: 0; top: 355px;
    display: flex; justify-content: center; align-items: center; gap: 22px;
    font-size: 56px; font-weight: 800; color: var(--leaf-deep); line-height: 1;
  }
  .hotline__icon { width: 42px; height: 42px; }
</style>
</head>
<body>
<main class="canvas">
  <section class="card card--front" aria-label="Card front">
    <div class="brand">
      <span class="brand__name-top">VERGE</span>
      <span class="brand__name-bottom">CREW</span>
      <span class="brand__slogan">Call The Pellows</span>
    </div>
    <div class="divider"></div>
    <div class="contact">
      <h1 class="contact__name">MILO PELLOW</h1>
      <ul class="contact__list">
        <li class="contact__item">
          <svg class="contact__icon" viewBox="0 0 24 24"><path fill="#1d4a26" d="M6.6 10.8a15 15 0 0 0 6.6 6.6l2.2-2.2a1 1 0 0 1 1-.25 11.4 11.4 0 0 0 3.6.57 1 1 0 0 1 1 1V20a1 1 0 0 1-1 1A17 17 0 0 1 3 4a1 1 0 0 1 1-1h3.5a1 1 0 0 1 1 1c0 1.25.2 2.45.57 3.57a1 1 0 0 1-.25 1z"/></svg>
          0493 218 067</li>
        <li class="contact__item">
          <svg class="contact__icon" viewBox="0 0 24 24"><path fill="#1d4a26" d="M3 5h18v14H3z"/><path fill="none" stroke="#e9f5d8" stroke-width="1.8" d="M3.5 6l8.5 7 8.5-7"/></svg>
          vergecrew@postbox-example.com</li>
        <li class="contact__item">
          <svg class="contact__icon" viewBox="0 0 24 24"><rect x="4" y="4" width="16" height="16" rx="2" fill="#1d4a26"/></svg>
          vergecrew-example.com.au</li>
        <li class="contact__item">
          <svg class="contact__icon" viewBox="0 0 24 24"><circle cx="12" cy="12" r="8" fill="none" stroke="#1d4a26" stroke-width="3"/></svg>
          vergecrew</li>
      </ul>
    </div>
  </section>

  <section class="card card--back" aria-label="Card back">
    <h2 class="service">LAWN MOWING SERVICE</h2>
    <p class="qualities">LOCAL<span class="qualities__sep"></span>AFFORDABLE</p>
    <p class="includes"><span class="includes__text">EDGE TRIM, BLOW &amp; CLIPPING REMOVAL INCLUDED.</span></p>
    <p class="extras">OTHER GARDENING MATTERS, <span class="extras__ask">JUST ASK!</span></p>
    <p class="hotline">
      <svg class="hotline__icon" viewBox="0 0 24 24"><path fill="#46a51f" d="M6.6 10.8a15 15 0 0 0 6.6 6.6l2.2-2.2a1 1 0 0 1 1-.25 11.4 11.4 0 0 0 3.6.57 1 1 0 0 1 1 1V20a1 1 0 0 1-1 1A17 17 0 0 1 3 4a1 1 0 0 1 1-1h3.5a1 1 0 0 1 1 1c0 1.25.2 2.45.57 3.57a1 1 0 0 1-.25 1z"/></svg>
      <span>0493 218 067</span>
    </p>
  </section>
</main>
</body>
</html>
```